Honigetikett gesucht
Zielgruppe
Ich bin ein Hobbyimker und brauche ein Etikett für meinen Honig. Zielgruppe = Jeder
Aufgabenstellung
Bitte keine schwarzen Etiketten mehr... gefällt uns leider nicht. Danke!
Das Etikett ist für Honig, 500 Gramm Glas. Man muss den gesetzlichen Vorgaben einhalten. https://www.wabenhof-vorlu.at/de/labor/lebensmittelrecht.html
Blütenhonig aus Österreich
Name
Adresse
500 g
Trocken und vor Licht und Wärme geschützt lagern.
Mindestens haltbar bis:
Sichtfeldregelung
Sachbezeichnung und Nettofüllmenge müssen am Etikett in einem Sichtfeld angebracht werden. Ein Sichtfeld ist eine Oberfläche einer Verpackung, die von einem einzigen Blickpunkt aus gelesen werden kann.
Mindesthaltbarkeitsdatum und Lagerbedingungen sind in einem Sichtfeld anzubringen. Dabei muss die Lagerbedingung über oder unter der Haltbarkeit angeführt werden und darf nicht durch Bild- oder Schrift getrennt sein.
Mindestschriftgröße aller verpflichtenden Angaben (Ausnahme Nettofüllmenge) Mindestschriftgröße:
Die verwendete Schrift muss am kleinen „x“ der verwendeten Schriftart gemessen mindestens 1,2mm Höhe ausmachen
Erreicht die Gesamtoberfläche des Gebindes auf dem Ein Etikett angebracht werden kann max. 80cm2, so muss die Höhe am kleinen „x“ der verwendeten Schriftart gemessen mindestens 0,9mm Höhe ausmachen (beim Honigglas wäre dies erst unter dem 125g Glas)
Die Mindestschriftgröße der Nettofüllmenge bleibt davon unberührt und unterliegt weiterhin der Fertigpackungsverordnung (siehe Nettofüllmenge)

```html
<!DOCTYPE html>
<html lang="de">
<head>
<meta charset="utf-8">
<title>Blütenhonig – Etikett</title>
<link rel="stylesheet" href="https://fonts.googleapis.com/css2?family=Amatic+SC:wght@700&family=Montserrat:wght@400;600;700&display=swap">
<style>
  :root {
    --canvas: #ffffff;
    --paper: #e5e0d8;
    --paper-light: #ebe7e0;
    --paper-shade: #dcd6cd;
    --ink: #2f2f2f;
  }
  html, body {
    margin: 0;
    padding: 0;
    width: 1200px;
    height: 1200px;
    overflow: hidden;
    background: var(--canvas);
  }
  .canvas {
    position: relative;
    width: 1200px;
    height: 1200px;
  }
  .label {
    position: absolute;
    left: 49px;
    top: 376px;
    width: 1102px;
    height: 499px;
    overflow: hidden;
    color: var(--ink);
    font-family: "Montserrat", sans-serif;
  }
  .label__floral {
    position: absolute;
    inset: 0;
    background: radial-gradient(ellipse at 50% 40%, var(--paper-light) 0%, var(--paper) 60%, var(--paper-shade) 100%);
  }
  .label__honeycomb {
    position: absolute;
    inset: 0;
    width: 1102px;
    height: 499px;
  }
  .cell--outline { fill: none; stroke: var(--ink); stroke-width: 3; }
  .cell--solid { fill: var(--ink); }

  .product-name {
    position: absolute;
    left: 0;
    width: 100%;
    top: 170px;
    margin: 0;
    text-align: center;
    font-family: "Amatic SC", cursive;
    font-weight: 700;
    font-size: 100px;
    line-height: 1;
    letter-spacing: 1px;
    text-transform: uppercase;
  }
  .origin {
    position: absolute;
    left: 0;
    width: 100%;
    top: 276px;
    margin: 0;
    text-align: center;
    font-size: 38px;
    font-weight: 400;
    line-height: 1;
    letter-spacing: 0.5px;
  }
  .net-quantity {
    position: absolute;
    left: 0;
    width: 100%;
    top: 369px;
    margin: 0;
    text-align: center;
    font-size: 36px;
    font-weight: 400;
    line-height: 1;
  }
  .net-quantity__mark {
    font-family: "Montserrat", sans-serif;
    font-weight: 700;
    margin-right: 18px;
  }
  .best-before {
    position: absolute;
    left: 50px;
    top: 278px;
    margin: 0;
    font-size: 16px;
    line-height: 19px;
  }
  .best-before strong { font-weight: 700; }
  .storage {
    position: absolute;
    left: 50px;
    top: 324px;
    margin: 0;
    font-size: 11.4px;
    line-height: 15px;
  }
  .producer {
    position: absolute;
    left: 50px;
    top: 394px;
    margin: 0;
    font-style: normal;
    font-size: 16px;
    line-height: 21px;
  }
</style>
</head>
<body>
<div class="canvas">
  <section class="label">
    <div class="label__floral" role="img" aria-label="Zarte Blütenzeichnung mit Blüten und Blättern in hellen Beigetönen als Hintergrund"></div>

    <svg class="label__honeycomb" viewBox="0 0 1296 586" aria-hidden="true">
      <defs>
        <polygon id="cell" points="-75,0 -37.5,-65 37.5,-65 75,0 37.5,65 -37.5,65"/>
      </defs>
      <!-- left cluster -->
      <use href="#cell" class="cell--outline" transform="translate(125 97)"/>
      <use href="#cell" class="cell--solid" transform="translate(258 19)"/>
      <use href="#cell" class="cell--outline" transform="translate(258 174)"/>
      <!-- right cluster -->
      <use href="#cell" class="cell--outline" transform="translate(1167 80)"/>
      <use href="#cell" class="cell--solid" transform="translate(1167 234)"/>
      <use href="#cell" class="cell--outline" transform="translate(1298 310)"/>
      <use href="#cell" class="cell--outline" transform="translate(1167 387)"/>
      <use href="#cell" class="cell--solid" transform="translate(1037 458)"/>
      <use href="#cell" class="cell--outline" transform="translate(1298 462)"/>
      <use href="#cell" class="cell--outline" transform="translate(1037 612)"/>
    </svg>

    <h1 class="product-name">Blütenhonig</h1>
    <p class="origin">aus Österreich</p>
    <p class="net-quantity"><span class="net-quantity__mark">℮</span>500g</p>

    <p class="best-before">Mindestens haltbar<br>bis: <strong>09/2023</strong></p>
    <p class="storage">Trocken und vor Licht und<br>Wärme geschützt lagern.</p>

    <address class="producer">Ilse Tormann<br>Kleehofgasse 4b<br>3500 Krems</address>
  </section>
</div>
</body>
</html>
```